Upmarket cover for top management book, ideally unlike most common cover pages

This book is about both good management and mismanagement and introduces novel concepts such as the inverse exponential law in strategy, No doubt that these concepts will be criticized by some management scholars. However, students, a few other colleagues and key top managers find the new ideas useful and eye-opening.
The cover must help communicate a deeper vision of management as an expression of life creation and a sort of "divine" energy.

Practical details:
Print and ebook cover page plus elements of the cover for each of the three main book sections.
Title; The Harbor
Subtitle: Field methods and the quiet ripple rule
Author: Teodor M. Vasquel
Publisher: Brightwell Page Press
Width x height: 13,97 x 21,59 cm (without bleed)
Spine: 14-15 cm according to paper color

Target Market(s)

Mostly managers who did not have the opportunity of attending postgraduate management studies such as the MBA

Industry/Entity Type

Mostly high technology

Font styles to use
Serif
Sans Serif
Other font styles liked:
• Arial nova, Arial light

Requirements
Must have
• Preferably cover and back cover on white background, but any good proposals would do.
Nice to have
• An image of bright and reassuring, albeit potentially unlimited, strength. Ideally the cover design should show that good management is good for the COMMON GOOD of society
Should not have
• Please do not show images of people and no proposals reminiscent of other management and strategy book covers

```html
<!DOCTYPE html>
<html lang="en">
<head>
<meta charset="utf-8">
<title>The Harbor – Book Cover</title>
<link href="https://fonts.googleapis.com/css2?family=Montserrat:wght@600;700&family=Crimson+Pro:wght@300;400&family=Libre+Baskerville:wght@400;700&display=swap" rel="stylesheet">
<style>
  :root {
    --backdrop: #c6c7c9;
    --paper: #f4f4f4;
    --spine-paper: #ececec;
    --ink-dark: #333335;
    --ink-red: #e0302f;
    --ink-grey: #555558;
    --band: #3a3a3c;
    --key-tone-a: #d9d9db;
    --key-tone-b: #8a8a8e;
    --press-accent: #e9a83a;
  }
  * { box-sizing: border-box; margin: 0; padding: 0; }
  html, body {
    width: 1200px; height: 900px; overflow: hidden;
    background: var(--backdrop);
  }
  .book-wrap {
    position: absolute; left: 117px; top: 100px;
    width: 966px; height: 700px;
    display: flex;
  }
  .back-cover, .front-cover, .spine {
    position: relative; height: 700px; background: var(--paper); overflow: hidden;
  }
  .back-cover, .front-cover { width: 453px; }
  .spine { width: 60px; background: var(--spine-paper); border-left: 1px solid #dcdcdc; border-right: 1px solid #dcdcdc; }

  .sans { font-family: "Montserrat", Arial, sans-serif; font-weight: 600; }
  .serif { font-family: "Libre Baskerville", Georgia, serif; }

  .key-art {
    position: absolute; border-radius: 6px;
    background: linear-gradient(160deg, var(--key-tone-a), var(--key-tone-b));
    opacity: .55;
  }

  /* Front cover */
  .front-cover .top-strip { position: absolute; left: 165px; top: 60px; width: 220px; height: 22px; background: var(--band); }
  .front-cover .author {
    position: absolute; left: 48px; top: 88px;
    font-family: "Crimson Pro", Georgia, serif; font-weight: 300;
    font-size: 30px; color: var(--ink-grey);
  }
  .front-cover .the-band {
    position: absolute; left: 40px; top: 132px; width: 230px; height: 42px; background: var(--band);
  }
  .front-cover .the-band span {
    position: absolute; left: 12px; top: 4px; color: #fff; font-size: 32px;
  }
  .front-cover .key-art { left: 270px; top: 92px; width: 150px; height: 205px; }
  .title-letter { position: absolute; font-size: 132px; line-height: 1; }
  .dark { color: var(--ink-dark); }
  .red { color: var(--ink-red); }
  .front-cover .subtitle-band {
    position: absolute; left: 40px; top: 605px; width: 390px; height: 38px; background: var(--band);
    display: flex; align-items: center; justify-content: flex-end; padding-right: 14px;
  }
  .front-cover .subtitle-band span { color: #fff; font-size: 11.5px; letter-spacing: .4px; white-space: nowrap; }

  /* Spine */
  .spine-text {
    position: absolute; left: 50%; white-space: nowrap;
    transform-origin: left top; transform: rotate(90deg);
  }
  .spine-subtitle { top: 24px; margin-left: 7px; font-size: 8.5px; color: var(--ink-dark); }
  .spine-title { top: 300px; margin-left: 14px; font-size: 24px; color: var(--ink-red); letter-spacing: 1px; }
  .spine .key-art { left: 18px; top: 500px; width: 24px; height: 40px; }
  .press-mark {
    position: absolute; bottom: 60px; left: 50%; transform: translateX(-50%);
    display: flex; flex-direction: column; align-items: center; gap: 6px;
  }
  .press-mark .square { width: 18px; height: 18px; background: var(--press-accent); }
  .press-mark .name { font-size: 6.5px; color: var(--ink-dark); text-align: center; line-height: 1.3; }

  /* Back cover */
  .mini-title { position: absolute; left: 44px; top: 60px; width: 220px; height: 170px; }
  .mini-title .the { position: absolute; left: 0; top: 0; font-size: 12px; color: var(--ink-red); }
  .mini-title .l { position: absolute; font-size: 40px; line-height: 1; }
  .mini-title .key-art { left: 130px; top: 0; width: 70px; height: 70px; }
  .blurb {
    position: absolute; left: 44px; top: 250px; width: 370px;
    font-size: 11.5px; line-height: 1.55; color: #2a2a2a; text-align: justify;
  }
  .blurb p + p { margin-top: 18px; }
  .endorser { margin-top: 28px; font-size: 11.5px; line-height: 1.5; text-align: left; }
  .endorser strong { display: block; font-weight: 700; }
</style>
</head>
<body>
  <div class="book-wrap">

    <section class="back-cover">
      <div class="mini-title sans">
        <span class="the">THE</span>
        <span class="l dark" style="left:0;top:20px">H</span>
        <span class="l red" style="left:42px;top:20px">A</span>
        <div class="key-art" role="img" aria-label="Illustration of a ring of old keys"></div>
        <span class="l red" style="left:20px;top:70px">R</span>
        <span class="l dark" style="left:66px;top:70px">B</span>
        <span class="l dark" style="left:40px;top:120px">O</span>
        <span class="l red" style="left:86px;top:120px">R</span>
      </div>
      <div class="blurb serif">
        <p>Professor Vasquel, an Italian, has produced a provocative treatise that is worthy of Orsino Dalvi and other great thinkers and places their discoveries in the real world of human organizations, to see whether science can contribute to making a manager's job any easier in the competitive marketplace. To my knowledge, this is a pioneering idea. In brief, just as the chemist Anselm Rocca turned to literature, the chemist Teodor Vasquel uses the laws of the universe on the manager.</p>
        <p>I am reminded of the firm Verano Pianoforte who changed the piano in the 20th century. Verano applied the principles of acoustic engineering and physics to the business of constructing handcrafted pianos that produce beautiful music all over the world. The author goes one step further: he applies hard science to the soft art of management. The results, as you might expect, are eye-opening.</p>
        <div class="endorser">
          <strong>Martin R. Ellory</strong>
          Professor of Strategic Management, Eastmoor Campus University
        </div>
      </div>
    </section>

    <section class="spine">
      <span class="spine-text spine-subtitle serif">FIELD METHODS AND THE QUIET RIPPLE RULE</span>
      <span class="spine-text spine-title sans">THE HARBOR</span>
      <div class="key-art" role="img" aria-label="Small illustration of a ring of keys"></div>
      <div class="press-mark">
        <span class="square"></span>
        <span class="name serif">Brightwell<br>Page Press</span>
      </div>
    </section>

    <section class="front-cover">
      <div class="top-strip"></div>
      <div class="author">Teodor M. Vasquel</div>
      <div class="the-band"><span class="sans">THE</span></div>
      <div class="key-art" role="img" aria-label="Illustration of a large ring holding old-fashioned keys"></div>
      <span class="title-letter sans dark" style="left:38px;top:170px">H</span>
      <span class="title-letter sans red" style="left:150px;top:170px">A</span>
      <span class="title-letter sans red" style="left:70px;top:310px">R</span>
      <span class="title-letter sans dark" style="left:188px;top:310px">B</span>
      <span class="title-letter sans dark" style="left:165px;top:450px">O</span>
      <span class="title-letter sans red" style="left:300px;top:450px">R</span>
      <div class="subtitle-band"><span class="serif">FIELD METHODS AND THE QUIET RIPPLE RULE</span></div>
    </section>

  </div>
</body>
</html>
```